Flyer Design for a Boston Therapeutic Clinic

I am a body therapist who needs a couple of flyers designed:
1. To fit half a page.
2. To fit a 5 inch by 3.5 inch flyer.
My practice is based in Boston, MA and my web site is:
www.LarchTessvik.Com
For the First half page:
A. Have my company's name and color shown as it appears on my web site (Larch Tessvik)
B. Have the following text: "Control your weight (This part should be emphasized) by balancing your nervous and digestive system through the Tessvik Method. The Tessvik Method, a technique developed by Dr. Mara. Tessvik, uses physical pressure to manipulate visceral tissue to bring back resiliency and proper functioning of the whole body."
Also helps with
-Constipation
-Bloating
-IBS
-eating disorders and overeating
Our practitioner is highly experienced. Please visit our web sites for reviews.
C. I would like to have a nice earthy feeling, something that feels "freeing" like open flowers, or an open land scape such as mountains or fields.
D. I also like the color blue, white, orange; perhaps if these colors can be integrated into the flyer, that would be great.
E. "Visit our web site LarchTessvik.com or call 786-555-0148"
The Smaller Flyer :
A.The smaller Flyer should also have my Company's name as shown on my web site (Larch Tessvik)
B.The following text: " Restore your body's natural resiliency and greatly reduce your physical pain through the Dr. Mara Tessvik Method of Structural Integration."
C. "Our practitioner is highly experienced and has a great reputation; visit our web site for reviews."
"Benefits:
"reduce aches and pains
reduce joint pain
reduce chronic muscular tension"
D, "feel better after the first session!"
E. if you could use a picture of me working on someone from my web site, that would be great.
F. I also like the colors white, orange and silver, for this one.
G. "Visit our web site LarchTessvik.com or call 786-555 0148"
I am very open minded,
I would like the flyer to evoke a sense of tranquility, professionalism, and simplicity. So if you have another angle you think would look good, then go for it! As long as it looks clean, professional and helpful.
Thanks a lot!
If you need any pictures from my web site, I have the original high resolution files that i can send.
Professionals and working men and women from ages 20-70
Clinic

```html
<!DOCTYPE html>
<html lang="en">
<head>
<meta charset="utf-8">
<title>Larch Tessvik Therapy – Flyers</title>
<link rel="stylesheet" href="https://fonts.googleapis.com/css2?family=Zilla+Slab:wght@300;400&family=Roboto+Condensed:wght@400;700&family=Roboto:wght@400;500&display=swap">
<style>
  :root {
    --backdrop: #6f6f6f;
    --paper: #ffffff;
    --paper-shade: #ececec;
    --orange: #ee6a2a;
    --orange-bright: #f7931e;
    --yellow: #ffd21f;
    --yellow-text: #f4e23a;
    --ink: #1e1e1e;
    --grey-title: #6b6b6b;
    --blue-top: #2f8fd6;
    --blue-bottom: #1c2a6e;
    --silver-light: #f3f3f3;
    --silver-dark: #a9adb2;
    --bullet: #d93a2b;
  }
  * { box-sizing: border-box; margin: 0; padding: 0; }
  html, body { width: 1200px; height: 543px; overflow: hidden; }
  body { background: var(--backdrop); position: relative; font-family: "Roboto", Arial, sans-serif; color: var(--ink); }

  .flyer { position: absolute; background: var(--paper); overflow: hidden; box-shadow: 0 2px 6px rgba(0,0,0,.35); }

  /* Half-page flyer */
  .flyer--half { left: 30px; top: 26px; width: 691px; height: 489px;
    background: radial-gradient(ellipse at 40% 55%, #ffffff 40%, var(--paper-shade) 100%); }
  .half__photo { position: absolute; left: 0; top: 0; width: 100%; height: 190px;
    background: linear-gradient(180deg, #bcd3ea 0%, #d9dfe4 30%, #8c8690 50%, #b5683c 72%, #c7502a 86%, #d88a3a 100%); }
  .half__rule { position: absolute; left: 0; top: 190px; width: 100%; height: 5px; background: var(--orange-bright); }
  .brand { font-family: "Zilla Slab", Georgia, serif; font-weight: 300; white-space: nowrap; letter-spacing: .5px; }
  .brand__first { color: var(--orange); }
  .brand__rest { color: var(--grey-title); }
  .half__brand { position: absolute; right: 34px; top: 210px; font-size: 34px; line-height: 40px; }
  .half__headline { position: absolute; left: 34px; top: 270px; font-family: "Roboto Condensed", Arial Narrow, sans-serif;
    font-weight: 400; color: var(--orange); font-size: 23px; line-height: 28px; }
  .half__body { position: absolute; left: 34px; top: 300px; width: 370px; font-size: 13px; line-height: 16.8px; text-align: justify; }
  .half__also { position: absolute; left: 445px; top: 268px; font-size: 13.5px; }
  .half__also-title { margin-bottom: 10px; }
  .conditions { list-style: none; }
  .conditions li { display: flex; align-items: center; gap: 7px; height: 21px; font-size: 14px; }
  .conditions li::before { content: ""; width: 8px; height: 8px; border-radius: 50%;
    background: radial-gradient(circle at 35% 35%, #ff9a8a, var(--bullet) 60%, #8a1a10); }
  .half__band-rule { position: absolute; left: 0; top: 402px; width: 100%; height: 5px; background: var(--orange-bright); }
  .half__band { position: absolute; left: 0; top: 407px; width: 100%; height: 67px;
    background: linear-gradient(180deg, var(--blue-top) 0%, #26508f 55%, var(--blue-bottom) 100%); text-align: center; }
  .half__band-note { color: var(--yellow-text); font-size: 14px; padding-top: 8px; }
  .half__band-cta { color: var(--orange-bright); font-weight: 500; font-size: 21px; letter-spacing: .3px; margin-top: 5px; }
  .half__foot { position: absolute; left: 0; top: 474px; width: 100%; height: 15px;
    background: linear-gradient(90deg, var(--orange) 0%, var(--yellow) 50%, var(--orange) 100%); }

  /* Small flyer */
  .flyer--small { left: 746px; top: 51px; width: 419px; height: 294px; }
  .small__photo { position: absolute; left: 232px; top: 0; width: 187px; height: 253px;
    background: radial-gradient(ellipse at 55% 60%, #c5502c 0%, #a83a22 45%, #d86a22 75%, #f08a20 100%); }
  .small__brand { position: absolute; left: 20px; top: 19px; font-size: 17.5px; line-height: 20px; }
  .small__rule { position: absolute; left: 0; top: 42px; width: 232px; height: 3px;
    background: linear-gradient(90deg, #ffffff, var(--silver-dark)); }
  .small__text { position: absolute; left: 20px; width: 200px; font-size: 8.8px; line-height: 11px; text-align: justify; }
  .small__text--intro { top: 56px; }
  .small__text--reputation { top: 101px; }
  .small__benefits-title { position: absolute; left: 20px; top: 157px; color: var(--orange); font-weight: 500; font-size: 10.5px; }
  .benefits { position: absolute; left: 20px; top: 175px; list-style: none; }
  .benefits li { display: flex; align-items: center; gap: 5px; height: 17.6px; font-size: 9.5px; color: #333; }
  .benefits svg { width: 10px; height: 10px; }
  .small__tagline { position: absolute; left: 20px; top: 234px; color: var(--orange); font-family: "Roboto Condensed", Arial Narrow, sans-serif;
    font-size: 12px; font-weight: 400; }
  .small__band { position: absolute; left: 0; top: 253px; width: 100%; height: 26px;
    background: linear-gradient(180deg, var(--silver-light) 0%, #d4d7da 50%, var(--silver-dark) 100%);
    border-top: 2px solid #8d9196; text-align: center; }
  .small__band-cta { color: var(--orange); font-weight: 500; font-size: 13px; line-height: 22px; letter-spacing: .2px; }
  .small__foot { position: absolute; left: 0; top: 281px; width: 100%; height: 13px;
    background: linear-gradient(90deg, var(--orange) 0%, var(--yellow) 50%, var(--orange) 100%); }
</style>
</head>
<body>

<section class="flyer flyer--half" aria-label="Half-page flyer">
  <div class="half__photo" role="img" aria-label="Open mountain valley landscape with autumn-coloured fields under a blue sky"></div>
  <div class="half__rule"></div>
  <h1 class="brand half__brand"><span class="brand__first">Larch</span> <span class="brand__rest">Tessvik Therapy</span></h1>
  <h2 class="half__headline">Control your weight</h2>
  <p class="half__body">by balancing your nervous and digestive system through the Tessvik Method. The Tessvik Method, a technique developed by Dr. Mara. Tessvik, uses physical pressure to manipulate visceral tissue to bring back resiliency and proper functioning of the whole body.</p>
  <div class="half__also">
    <p class="half__also-title">Also helps with</p>
    <ul class="conditions">
      <li>Constipation</li>
      <li>Bloating</li>
      <li>IBS</li>
      <li>eating disorders and overeating</li>
    </ul>
  </div>
  <div class="half__band-rule"></div>
  <div class="half__band">
    <p class="half__band-note">Our practitioner is highly experienced. Please visit our web sites for reviews.</p>
    <p class="half__band-cta">Visit our web site LarchTessvik.com or call 786-555-0148</p>
  </div>
  <div class="half__foot"></div>
</section>

<section class="flyer flyer--small" aria-label="Small flyer">
  <h1 class="brand small__brand"><span class="brand__first">Larch</span> <span class="brand__rest">Tessvik Therapy</span></h1>
  <div class="small__rule"></div>
  <p class="small__text small__text--intro">Restore your body's natural resiliency and greatly reduce your physical pain through the Dr. Mara Tessvik Method of Structural Integration.</p>
  <p class="small__text small__text--reputation">Our practitioner is highly experienced and has a great reputation; visit our web site for reviews.physical pain through the Dr. Mara Tessvik Method of Structural Integration.</p>
  <p class="small__benefits-title">Benefits:</p>
  <ul class="benefits">
    <li><svg viewBox="0 0 10 10" aria-hidden="true"><rect x="0.6" y="1.6" width="7.8" height="7.8" fill="none" stroke="#ee6a2a" stroke-width="1.1"/><path d="M2.2 5.2 L4.2 7.3 L9.4 0.8" fill="none" stroke="#ee6a2a" stroke-width="1.4"/></svg>reduce aches and pains</li>
    <li><svg viewBox="0 0 10 10" aria-hidden="true"><rect x="0.6" y="1.6" width="7.8" height="7.8" fill="none" stroke="#ee6a2a" stroke-width="1.1"/><path d="M2.2 5.2 L4.2 7.3 L9.4 0.8" fill="none" stroke="#ee6a2a" stroke-width="1.4"/></svg>reduce joint pain</li>
    <li><svg viewBox="0 0 10 10" aria-hidden="true"><rect x="0.6" y="1.6" width="7.8" height="7.8" fill="none" stroke="#ee6a2a" stroke-width="1.1"/><path d="M2.2 5.2 L4.2 7.3 L9.4 0.8" fill="none" stroke="#ee6a2a" stroke-width="1.4"/></svg>reduce chronic muscular tension</li>
  </ul>
  <p class="small__tagline">feel better after the first session!</p>
  <div class="small__photo" role="img" aria-label="Practitioner working on a client's shoulder and upper back in a warmly lit treatment room"></div>
  <div class="small__band"><p class="small__band-cta">Visit our web site LarchTessvik.com or call 786-555-0148</p></div>
  <div class="small__foot"></div>
</section>

</body>
</html>
```